edgy fitness flyer

Utilize quote
"I don't want a great body"
by: Nobody Ever
Offer oin back . Vard needs to be edgy and sexy.

Target Market(s)

Women and men 25-45

Industry/Entity Type

Fitness

Requirements
Must have
• clear font layered over gradient image
• See attached sample.
• bright and eye catching
• must coordniate with studio image
• www.plovarfitness.com

```html
<!DOCTYPE html>
<html lang="en">
<head>
<meta charset="utf-8">
<title>I Don't Want a Great Body – Fitness Flyer</title>
<link rel="stylesheet" href="https://fonts.googleapis.com/css2?family=Saira+Stencil+One&family=Lobster&family=Black+Ops+One&family=Oswald:wght@600;700&display=swap">
<style>
  :root {
    --ink-black: #0b0b0b;
    --concrete-light: #d6d6d4;
    --concrete-mid: #7d7d7b;
    --concrete-dark: #262626;
    --rust-orange: #f07a1a;
    --rust-deep: #c9560c;
    --volt-yellow: #e6ef1c;
    --url-orange: #f7931e;
  }
  html, body {
    margin: 0;
    padding: 0;
    width: 816px;
    height: 1200px;
    overflow: hidden;
    background: var(--ink-black);
  }
  .flyer {
    position: relative;
    width: 816px;
    height: 1200px;
    overflow: hidden;
    background: var(--concrete-dark);
  }
  .concrete-backdrop {
    position: absolute;
    inset: 0;
    background:
      radial-gradient(ellipse 14% 6% at 14% 30%, rgba(240,122,26,0.55) 0%, rgba(240,122,26,0) 100%),
      radial-gradient(ellipse 10% 5% at 8% 68%, rgba(240,122,26,0.45) 0%, rgba(240,122,26,0) 100%),
      radial-gradient(ellipse 12% 4% at 40% 57%, rgba(240,122,26,0.4) 0%, rgba(240,122,26,0) 100%),
      radial-gradient(ellipse 10% 5% at 92% 52%, rgba(240,122,26,0.35) 0%, rgba(240,122,26,0) 100%),
      radial-gradient(ellipse 9% 4% at 48% 79%, rgba(240,122,26,0.35) 0%, rgba(240,122,26,0) 100%),
      radial-gradient(ellipse 8% 4% at 88% 3%, rgba(240,122,26,0.4) 0%, rgba(240,122,26,0) 100%),
      radial-gradient(ellipse 22% 10% at 78% 20%, rgba(20,20,20,0.7) 0%, rgba(20,20,20,0) 100%),
      radial-gradient(ellipse 20% 9% at 12% 10%, rgba(15,15,15,0.75) 0%, rgba(15,15,15,0) 100%),
      radial-gradient(ellipse 18% 8% at 90% 66%, rgba(25,25,25,0.6) 0%, rgba(25,25,25,0) 100%),
      radial-gradient(ellipse 55% 38% at 62% 40%, rgba(225,225,222,0.9) 0%, rgba(150,150,148,0.55) 45%, rgba(60,60,60,0) 80%),
      radial-gradient(ellipse 60% 22% at 45% 14%, rgba(200,200,198,0.6) 0%, rgba(0,0,0,0) 75%),
      linear-gradient(180deg, #3c3c3b 0%, #5a5a58 30%, #3a3a39 62%, #1a1a1a 82%, #0e0e0e 100%);
  }
  .athlete-photo {
    position: absolute;
    left: 0;
    top: 417px;
    width: 310px;
    height: 540px;
    background:
      radial-gradient(ellipse 40% 16% at 55% 12%, #9a6a52 0%, rgba(154,106,82,0) 100%),
      linear-gradient(180deg, #3e2a22 0%, #a87660 18%, #b88a72 30%, #ededed 42%, #e4e4e4 85%, #1a1a1a 100%);
  }
  .type-layer {
    position: absolute;
    inset: 0;
    width: 816px;
    height: 1200px;
  }
  .stencil { font-family: "Saira Stencil One", sans-serif; }
  .script { font-family: "Lobster", cursive; }
  .plate { font-family: "Black Ops One", sans-serif; }
  .attribution { font-family: "Oswald", sans-serif; font-weight: 600; }
  .web-address { font-family: "Oswald", sans-serif; font-weight: 700; }
</style>
</head>
<body>
<main class="flyer">
  <div class="concrete-backdrop"></div>

  <div class="athlete-photo" role="img" aria-label="Photo of a woman in a white tank top swinging a kettlebell at arm's length"></div>

  <svg class="type-layer" viewBox="0 0 816 1200">
    <defs>
      <linearGradient id="chalk-fill" x1="0" y1="0" x2="0" y2="1">
        <stop offset="0" stop-color="#ffffff"/>
        <stop offset="0.5" stop-color="#ededed"/>
        <stop offset="0.72" stop-color="#f4a766"/>
        <stop offset="1" stop-color="#e46f12"/>
      </linearGradient>
      <linearGradient id="script-fill" x1="0" y1="0" x2="0" y2="1">
        <stop offset="0" stop-color="#ffa04a"/>
        <stop offset="0.5" stop-color="#f07a1a"/>
        <stop offset="1" stop-color="#c9560c"/>
      </linearGradient>
      <linearGradient id="steel-fill" x1="0" y1="0" x2="0" y2="1">
        <stop offset="0" stop-color="#c4c4c4"/>
        <stop offset="0.5" stop-color="#929292"/>
        <stop offset="1" stop-color="#5e5e5e"/>
      </linearGradient>
    </defs>
    <g role="heading" aria-level="1" aria-label="I don't want a great body">
      <text class="stencil" x="29" y="262" font-size="330" textLength="772" lengthAdjust="spacingAndGlyphs" fill="url(#chalk-fill)">I DON'T</text>
      <text class="script" x="140" y="372" font-size="175" textLength="558" lengthAdjust="spacingAndGlyphs" fill="url(#script-fill)" stroke="#7a3304" stroke-width="1.5">Want a</text>
      <text class="plate" x="294" y="532" font-size="150" textLength="426" lengthAdjust="spacingAndGlyphs" fill="url(#steel-fill)" stroke="#2e2e2e" stroke-width="2">GREAT</text>
      <text class="stencil" x="279" y="790" font-size="292" textLength="522" lengthAdjust="spacingAndGlyphs" fill="url(#chalk-fill)">BODY</text>
    </g>
    <text class="attribution" x="397" y="902" font-size="66" textLength="394" lengthAdjust="spacingAndGlyphs" fill="var(--volt-yellow)">BY:NOBODY EVER</text>
    <text class="web-address" x="154" y="1114" font-size="44" textLength="493" lengthAdjust="spacing" fill="var(--url-orange)">WWW.PLOVARFITNESS.COM</text>
  </svg>
</main>
</body>
</html>
```